1" x 3" label needed for essential oil bottle(s) - new ecommerce company

We need a label designed for 10 ml bottles of essential oils. We are offering 9 different types of essential oil: Lavender, Cedarwood, Eucalyptus, Frankincense, Lemon, Orange, Peppermint, Rosemary, and Tea Tree. The label should have a space for the type of essential oil. The bottles are an amber color (am including a photo) as essential oils are sensitive to light. also am including an AI file of our logo, which we'd like included on the label; the logo file also contains our logo colors, a dark blue and light grey. We'd also like the following on the label: "CAUTION: EYE AND SKIN IRRITANT. Avoid contact with eyes and skin. Wash hands after handling. If eye contact occurs, flush with water for 15 minutes. Not intended for topical or internal use. Contains Essential Oils. KEEP OUT OF REACH OF CHILDREN."
Also "Ingredients: 100% pure essential oil, GC tested."
Also "0.33 fl oz (10 ml)
Finally, we will need to include a sideways bar code on the right side of the label, so need 3/8" of white space on the right of the label.
We'd like the label to be calming, but modern, friendly, and confident.

```html
<!DOCTYPE html>
<html lang="en">
<head>
<meta charset="utf-8">
<title>Veralune Essential Oil Labels</title>
<link rel="stylesheet" href="https://fonts.googleapis.com/css2?family=Josefin+Sans:wght@300;400&family=Lato:wght@400&family=Tinos&display=swap">
<style>
  :root {
    --canvas: #ffffff;
    --label-bg: #efe3d5;
    --ink: #2b2f36;
    --brand-ink: #4a525f;
    --band-text: #ffffff;
    --lavender: #a67bb5;
    --frankincense: #e8521f;
    --tea-tree: #a7c87e;
    --lemon: #f7b535;
    --cedarwood: #14913f;
    --rosemary: #1f381c;
    --peppermint: #0d6a39;
    --orange: #f4941c;
    --eucalyptus: #4b6a2d;
    --leaf: #6fa148;
    --leaf-dark: #3f6f2a;
  }
  * { box-sizing: border-box; margin: 0; padding: 0; }
  html, body {
    width: 1200px; height: 1000px; overflow: hidden;
    background: var(--canvas);
  }
  .sheet { position: relative; width: 1200px; height: 1000px; }

  .label {
    position: absolute;
    width: 90em; height: 29.8em;
    background: var(--label-bg);
    color: var(--ink);
    box-shadow: 0 1.4em 1.8em rgba(0,0,0,0.22);
    overflow: hidden;
  }
  .label--small { font-size: 4.02px; }
  .label--large { font-size: 10px; left: 150px; top: 652px; }

  .caution-title, .caution-text, .ingredients, .producer {
    position: absolute; font-family: "Tinos", "Times New Roman", serif;
    font-size: 1.1em; line-height: 1.3;
  }
  .caution-title { left: 1.64em; top: 4.9em; }
  .caution-text { left: 1.64em; top: 6.8em; width: 18.6em; }
  .ingredients { left: 1.64em; top: 18em; }
  .producer { left: 66.2em; top: 6.9em; font-size: 1.2em; }

  .badges { position: absolute; left: 1.6em; top: 24.2em; display: flex; gap: 1.3em; align-items: center; }
  .badge { display: block; border: 0.18em solid var(--ink); }
  .badge--round { width: 3.4em; height: 3.4em; border-radius: 50%; }
  .badge--square { width: 2.6em; height: 2.6em; }

  .plant {
    position: absolute; top: 2.6em; width: 12em; height: 17em;
    border-radius: 40% 40% 10% 10%;
    background: linear-gradient(180deg, var(--plant-top, var(--leaf)) 0%, var(--leaf-dark) 100%);
    opacity: 0.85;
  }
  .plant--left { left: 23.6em; }
  .plant--right { left: 59.5em; }

  .brand-mark {
    position: absolute; left: 44.9em; top: 3.6em;
    width: 3.4em; height: 3.4em; border-radius: 50%;
    border: 0.18em solid var(--brand-ink);
  }
  .brand-name {
    position: absolute; left: 22.8em; top: 12.2em; width: 47.7em;
    text-align: center; font-family: "Josefin Sans", "Helvetica", sans-serif;
    font-weight: 300; font-size: 1em; color: var(--brand-ink);
  }
  .brand-name span { font-size: 3em; letter-spacing: 0.3em; padding-left: 0.3em; }

  .oil-band {
    position: absolute; left: 22.8em; top: 17em; width: 47.7em; height: 5.2em;
    background: var(--band);
    display: flex; align-items: center; justify-content: center;
    font-family: "Josefin Sans", "Helvetica", sans-serif; font-weight: 400;
    color: var(--band-text);
  }
  .oil-band span { font-size: 3.3em; letter-spacing: 0.08em; line-height: 1; padding-top: 0.12em; }

  .purity, .volume {
    position: absolute; left: 22.8em; width: 47.7em; text-align: center;
    font-family: "Lato", "Helvetica", sans-serif; line-height: 1;
  }
  .purity { top: 24.4em; font-size: 1.6em; width: 29.8em; left: 14.25em; }
  .volume { top: 27.1em; font-size: 1.7em; width: 28.06em; left: 13.41em; }
  .purity { top: 15.2em; }
  .volume { top: 16em; }

  .label--lavender { --band: var(--lavender); --plant-top: #8d6aa8; }
  .label--frankincense { --band: var(--frankincense); --plant-top: #8aa94e; }
  .label--tea-tree { --band: var(--tea-tree); --plant-top: #9a8a86; }
  .label--lemon { --band: var(--lemon); --plant-top: #7fb552; }
  .label--cedarwood { --band: var(--cedarwood); --plant-top: #5a9a5a; }
  .label--rosemary { --band: var(--rosemary); --plant-top: #3a5a3a; }
  .label--peppermint { --band: var(--peppermint); --plant-top: #9a80a8; }
  .label--orange { --band: var(--orange); --plant-top: #f08a22; }
  .label--eucalyptus { --band: var(--eucalyptus); --plant-top: #7a9a52; }
</style>
</head>
<body>
<main class="sheet">

  <article class="label label--small label--lavender" style="left:25px;top:187px">
    <p class="caution-title">CAUTION: EYE AND SKIN IRRITANT.</p>
    <p class="caution-text">Avoid contact with eyes and skin. If eye contact occurs, flush with water for 15 minutes. Not intended for topical or internal use. KEEP OUT OF REACH OF CHILDREN</p>
    <p class="ingredients">Ingredients:<br>100% pure essential oil, GC tested</p>
    <div class="badges"><span class="badge badge--round"></span><span class="badge badge--square"></span></div>
    <div class="plant plant--left" role="img" aria-label="Illustration of a lavender sprig"></div>
    <div class="plant plant--right" role="img" aria-label="Illustration of a lavender sprig"></div>
    <span class="brand-mark"></span>
    <p class="brand-name"><span>VERALUNE</span></p>
    <div class="oil-band"><span>LAVENDER</span></div>
    <p class="purity">100% pure essential oil</p>
    <p class="volume">0.33 fl oz (10 ml)</p>
    <p class="producer">Produced by:<br>Veralune Inc<br>Bayside - FL USA</p>
  </article>

  <article class="label label--small label--frankincense" style="left:422px;top:187px">
    <p class="caution-title">CAUTION: EYE AND SKIN IRRITANT.</p>
    <p class="caution-text">Avoid contact with eyes and skin. If eye contact occurs, flush with water for 15 minutes. Not intended for topical or internal use. KEEP OUT OF REACH OF CHILDREN</p>
    <p class="ingredients">Ingredients:<br>100% pure essential oil, GC tested</p>
    <div class="badges"><span class="badge badge--round"></span><span class="badge badge--square"></span></div>
    <div class="plant plant--left" role="img" aria-label="Illustration of a frankincense branch"></div>
    <div class="plant plant--right" role="img" aria-label="Illustration of a frankincense branch"></div>
    <span class="brand-mark"></span>
    <p class="brand-name"><span>VERALUNE</span></p>
    <div class="oil-band"><span>FRANKINCENSE</span></div>
    <p class="purity">100% pure essential oil</p>
    <p class="volume">0.33 fl oz (10 ml)</p>
    <p class="producer">Produced by:<br>Veralune Inc<br>Bayside - FL USA</p>
  </article>

  <article class="label label--small label--tea-tree" style="left:806px;top:187px">
    <p class="caution-title">CAUTION: EYE AND SKIN IRRITANT.</p>
    <p class="caution-text">Avoid contact with eyes and skin. If eye contact occurs, flush with water for 15 minutes. Not intended for topical or internal use. KEEP OUT OF REACH OF CHILDREN</p>
    <p class="ingredients">Ingredients:<br>100% pure essential oil, GC tested</p>
    <div class="badges"><span class="badge badge--round"></span><span class="badge badge--square"></span></div>
    <div class="plant plant--left" role="img" aria-label="Illustration of a tea tree branch"></div>
    <div class="plant plant--right" role="img" aria-label="Illustration of a tea tree branch"></div>
    <span class="brand-mark"></span>
    <p class="brand-name"><span>VERALUNE</span></p>
    <div class="oil-band"><span>TEA TREE</span></div>
    <p class="purity">100% pure essential oil</p>
    <p class="volume">0.33 fl oz (10 ml)</p>
    <p class="producer">Produced by:<br>Veralune Inc<br>Bayside - FL USA</p>
  </article>

  <article class="label label--small label--lemon" style="left:25px;top:327px">
    <p class="caution-title">CAUTION: EYE AND SKIN IRRITANT.</p>
    <p class="caution-text">Avoid contact with eyes and skin. If eye contact occurs, flush with water for 15 minutes. Not intended for topical or internal use. KEEP OUT OF REACH OF CHILDREN</p>
    <p class="ingredients">Ingredients:<br>100% pure essential oil, GC tested</p>
    <div class="badges"><span class="badge badge--round"></span><span class="badge badge--square"></span></div>
    <div class="plant plant--left" role="img" aria-label="Illustration of a leafy herb sprig"></div>
    <div class="plant plant--right" role="img" aria-label="Illustration of a leafy herb sprig"></div>
    <span class="brand-mark"></span>
    <p class="brand-name"><span>VERALUNE</span></p>
    <div class="oil-band"><span>LEMON</span></div>
    <p class="purity">100% pure essential oil</p>
    <p class="volume">0.33 fl oz (10 ml)</p>
    <p class="producer">Produced by:<br>Veralune Inc<br>Bayside - FL USA</p>
  </article>

  <article class="label label--small label--cedarwood" style="left:422px;top:327px">
    <p class="caution-title">CAUTION: EYE AND SKIN IRRITANT.</p>
    <p class="caution-text">Avoid contact with eyes and skin. If eye contact occurs, flush with water for 15 minutes. Not intended for topical or internal use. KEEP OUT OF REACH OF CHILDREN</p>
    <p class="ingredients">Ingredients:<br>100% pure essential oil, GC tested</p>
    <div class="badges"><span class="badge badge--round"></span><span class="badge badge--square"></span></div>
    <div class="plant plant--left" role="img" aria-label="Illustration of a cedar frond"></div>
    <div class="plant plant--right" role="img" aria-label="Illustration of a cedar frond"></div>
    <span class="brand-mark"></span>
    <p class="brand-name"><span>VERALUNE</span></p>
    <div class="oil-band"><span>CEDARWOOD</span></div>
    <p class="purity">100% pure essential oil</p>
    <p class="volume">0.33 fl oz (10 ml)</p>
    <p class="producer">Produced by:<br>Veralune Inc<br>Bayside - FL USA</p>
  </article>

  <article class="label label--small label--rosemary" style="left:806px;top:327px">
    <p class="caution-title">CAUTION: EYE AND SKIN IRRITANT.</p>
    <p class="caution-text">Avoid contact with eyes and skin. If eye contact occurs, flush with water for 15 minutes. Not intended for topical or internal use. KEEP OUT OF REACH OF CHILDREN</p>
    <p class="ingredients">Ingredients:<br>100% pure essential oil, GC tested</p>
    <div class="badges"><span class="badge badge--round"></span><span class="badge badge--square"></span></div>
    <div class="plant plant--left" role="img" aria-label="Illustration of a rosemary sprig"></div>
    <div class="plant plant--right" role="img" aria-label="Illustration of a rosemary sprig"></div>
    <span class="brand-mark"></span>
    <p class="brand-name"><span>VERALUNE</span></p>
    <div class="oil-band"><span>ROSEMARY</span></div>
    <p class="purity">100% pure essential oil</p>
    <p class="volume">0.33 fl oz (10 ml)</p>
    <p class="producer">Produced by:<br>Veralune Inc<br>Bayside - FL USA</p>
  </article>

  <article class="label label--small label--peppermint" style="left:25px;top:468px">
    <p class="caution-title">CAUTION: EYE AND SKIN IRRITANT.</p>
    <p class="caution-text">Avoid contact with eyes and skin. If eye contact occurs, flush with water for 15 minutes. Not intended for topical or internal use. KEEP OUT OF REACH OF CHILDREN</p>
    <p class="ingredients">Ingredients:<br>100% pure essential oil, GC tested</p>
    <div class="badges"><span class="badge badge--round"></span><span class="badge badge--square"></span></div>
    <div class="plant plant--left" role="img" aria-label="Illustration of a flowering peppermint stem"></div>
    <div class="plant plant--right" role="img" aria-label="Illustration of a flowering peppermint stem"></div>
    <span class="brand-mark"></span>
    <p class="brand-name"><span>VERALUNE</span></p>
    <div class="oil-band"><span>PEPPERMIT</span></div>
    <p class="purity">100% pure essential oil</p>
    <p class="volume">0.33 fl oz (10 ml)</p>
    <p class="producer">Produced by:<br>Veralune Inc<br>Bayside - FL USA</p>
  </article>

  <article class="label label--small label--orange" style="left:422px;top:468px">
    <p class="caution-title">CAUTION: EYE AND SKIN IRRITANT.</p>
    <p class="caution-text">Avoid contact with eyes and skin. If eye contact occurs, flush with water for 15 minutes. Not intended for topical or internal use. KEEP OUT OF REACH OF CHILDREN</p>
    <p class="ingredients">Ingredients:<br>100% pure essential oil, GC tested</p>
    <div class="badges"><span class="badge badge--round"></span><span class="badge badge--square"></span></div>
    <div class="plant plant--left" role="img" aria-label="Illustration of an orange branch with fruit and blossom"></div>
    <div class="plant plant--right" role="img" aria-label="Illustration of an orange branch with fruit and blossom"></div>
    <span class="brand-mark"></span>
    <p class="brand-name"><span>VERALUNE</span></p>
    <div class="oil-band"><span>ORANGE</span></div>
    <p class="purity">100% pure essential oil</p>
    <p class="volume">0.33 fl oz (10 ml)</p>
    <p class="producer">Produced by:<br>Veralune Inc<br>Bayside - FL USA</p>
  </article>

  <article class="label label--small label--eucalyptus" style="left:806px;top:468px">
    <p class="caution-title">CAUTION: EYE AND SKIN IRRITANT.</p>
    <p class="caution-text">Avoid contact with eyes and skin. If eye contact occurs, flush with water for 15 minutes. Not intended for topical or internal use. KEEP OUT OF REACH OF CHILDREN</p>
    <p class="ingredients">Ingredients:<br>100% pure essential oil, GC tested</p>
    <div class="badges"><span class="badge badge--round"></span><span class="badge badge--square"></span></div>
    <div class="plant plant--left" role="img" aria-label="Illustration of a eucalyptus branch"></div>
    <div class="plant plant--right" role="img" aria-label="Illustration of a eucalyptus branch"></div>
    <span class="brand-mark"></span>
    <p class="brand-name"><span>VERALUNE</span></p>
    <div class="oil-band"><span>EUCALYPTUS</span></div>
    <p class="purity">100% pure essential oil</p>
    <p class="volume">0.33 fl oz (10 ml)</p>
    <p class="producer">Produced by:<br>Veralune Inc<br>Bayside - FL USA</p>
  </article>

  <article class="label label--large label--lemon">
    <p class="caution-title">CAUTION: EYE AND SKIN IRRITANT.</p>
    <p class="caution-text">Avoid contact with eyes and skin. If eye contact occurs, flush with water for 15 minutes. Not intended for topical or internal use. KEEP OUT OF REACH OF CHILDREN</p>
    <p class="ingredients">Ingredients:<br>100% pure essential oil, GC tested</p>
    <div class="badges"><span class="badge badge--round"></span><span class="badge badge--square"></span></div>
    <div class="plant plant--left" role="img" aria-label="Illustration of a leafy herb sprig with small flowers"></div>
    <div class="plant plant--right" role="img" aria-label="Illustration of a leafy herb sprig with small flowers"></div>
    <span class="brand-mark"></span>
    <p class="brand-name"><span>VERALUNE</span></p>
    <div class="oil-band"><span>LEMON</span></div>
    <p class="purity">100% pure essential oil</p>
    <p class="volume">0.33 fl oz (10 ml)</p>
    <p class="producer">Produced by:<br>Veralune Inc<br>Bayside - FL USA</p>
  </article>

</main>
</body>
</html>
```